Customer flyer

Hi there,

We need a flyer done for our father's business. It is called Tidal crest and the flyer will be distributed to realtors in British Columbia. He lends money to realtors when they have sold a home from the time subjects are removed from the transaction to when the sale closes. He is looking for a modern, classy look with the following information:

"Tidal Crest"

Realtor Pay Day upon Subject Removal

Did you know?

* Fees 100% tax deductable
* Same Day Service
* Confidential
* Low Rates

Your money from 738519 B.C. Ltd. and It can be directly deposited into your bank account or delivered to your office

For quote: call Gavin Merrow 250 555 0137

This is a small business so he doesn't have a logo and has never needed to do promotions before as it's run on word of mouth for the past 10 years. We are open to all ideas and suggestions - he is a finance guy so looking to you for the creative side :)

Thank you!

I don't like the phrase Realtor Pay Day upon subject removal. I think I prefer "Realtors! Celebrate Your Home sales upon subject removal" . Your thoughts?

Thank you

```html
<!DOCTYPE html>
<html lang="en">
<head>
<meta charset="utf-8">
<title>Tidal Crest – Realtor Flyer</title>
<link rel="stylesheet" href="https://fonts.googleapis.com/css2?family=Jost:wght@500;600;700&family=Montserrat:wght@600&display=swap">
<style>
  :root {
    --page: #ffffff;
    --panel-light: #f2f2f2;
    --panel-dark: #bdbec0;
    --ink: #111111;
    --brand-yellow: #ffee00;
    --band-yellow-1: #f4e51c;
    --band-yellow-2: #e3cf10;
    --note-green-1: #c9d2bd;
    --note-green-2: #7f9178;
    --note-green-3: #4f5f4c;
  }
  * { margin: 0; padding: 0; box-sizing: border-box; }
  html, body { width: 842px; height: 1200px; overflow: hidden; background: var(--page); }
  .flyer { position: relative; width: 842px; height: 1200px; font-family: "Jost", "Futura", sans-serif; color: var(--ink); }
  .flyer__shapes { position: absolute; inset: 0; }
  .brand {
    position: absolute; top: 88px; left: 0; width: 842px; text-align: center;
    font-family: "Montserrat", sans-serif; font-weight: 600; font-size: 84px; line-height: 1;
    color: var(--brand-yellow); text-shadow: 3px 3px 0 var(--ink);
  }
  .tagline {
    position: absolute; top: 222px; left: 0; width: 842px; text-align: center;
    font-weight: 600; font-size: 28px; line-height: 1;
  }
  .headline {
    position: absolute; top: 286px; left: 0; width: 842px; text-align: center;
    font-weight: 700; font-size: 76px; line-height: 1;
    -webkit-text-stroke: 0; paint-order: stroke fill;
    text-shadow: 0 0 6px #fff, 3px 3px 0 #fff, -3px -3px 0 #fff, 3px -3px 0 #fff, -3px 3px 0 #fff, 0 4px 0 #fff, 0 -4px 0 #fff, 4px 0 0 #fff, -4px 0 0 #fff;
  }
  .benefits { position: absolute; top: 384px; left: 100px; list-style: none; }
  .benefits li { font-weight: 600; font-size: 44px; line-height: 57px; }
  .benefits li::before { content: "- "; }
  .delivery {
    position: absolute; top: 650px; left: 100px; width: 500px;
    font-weight: 600; font-size: 23px; line-height: 31px;
  }
  .contact {
    position: absolute; top: 940px; left: 65px;
    font-weight: 600; font-size: 44px; line-height: 57px;
  }
</style>
</head>
<body>
<div class="flyer">
  <svg class="flyer__shapes" width="842" height="1200" viewBox="0 0 842 1200">
    <defs>
      <radialGradient id="panel-fill" cx="0.5" cy="0.55" r="0.7">
        <stop offset="0" stop-color="var(--panel-light)"/>
        <stop offset="1" stop-color="var(--panel-dark)"/>
      </radialGradient>
      <linearGradient id="band-fill" x1="0" y1="0" x2="1" y2="1">
        <stop offset="0" stop-color="var(--band-yellow-2)"/>
        <stop offset="1" stop-color="var(--band-yellow-1)"/>
      </linearGradient>
      <linearGradient id="notes-fill" x1="0" y1="0" x2="1" y2="1">
        <stop offset="0" stop-color="var(--note-green-1)"/>
        <stop offset="0.55" stop-color="var(--note-green-2)"/>
        <stop offset="1" stop-color="var(--note-green-3)"/>
      </linearGradient>
    </defs>
    <rect class="panel" x="20" y="25" width="802" height="843" fill="url(#panel-fill)"/>
    <polygon class="contact-band" points="20,878 557,878 445,1178 20,1178" fill="url(#band-fill)"/>
    <polygon class="notes-frame" points="642,621 822,621 822,1178 436,1178" fill="var(--page)"/>
    <polygon class="notes-area" role="img" aria-label="Pile of scattered banknotes" points="652,628 822,628 822,1178 449,1178" fill="url(#notes-fill)"/>
  </svg>

  <h1 class="brand">Tidal Crest</h1>
  <p class="tagline">Realtor Pay Day upon Subject Removal</p>
  <h2 class="headline">Did you know?</h2>
  <ul class="benefits">
    <li>Fees 100% tax deductable</li>
    <li>Same Day Service</li>
    <li>Confidential</li>
    <li>Low Rates</li>
  </ul>
  <p class="delivery">Your money from 738519 B.C. Ltd.<br>and It can be directly deposited into<br>your bank account<br>or delivered to your office</p>
  <p class="contact">For quote:<br>call Gavin Merrow<br>250 555 0137</p>
</div>
</body>
</html>
```